French Puns

Creation of a cover for a book on French plays on words.
The public is lovers of the French language
TITLE: The gentle phrases of Honoré Vasseline
SUB-TITLE: Witty words, wit of words
PUBLISHER (at the bottom of the page): Editions Plumeau
(See joined examples, previous books of the same author)
Size: 14 x 20.5 cm
Please note that the text on the cover is in French, not in English:
Fine phrases from Honoré Vasseline
Witty words, witty words (subtitle, smaller)
Plumeau Editions

```html
<!DOCTYPE html>
<html lang="fr">
<head>
<meta charset="utf-8">
<title>Jeux pleins de sens, sens des jeux</title>
<link rel="stylesheet" href="https://fonts.googleapis.com/css2?family=Oswald:wght@600&family=Roboto+Condensed:ital,wght@0,400;0,700;1,300&display=swap">
<style>
  :root {
    --backdrop: #c6c6c6;
    --paper: #ffffff;
    --ink: #2b2a2b;
    --accent-red: #e8284f;
    --accent-yellow: #f7b347;
    --accent-orange: #f5a93a;
    --text-light: #ffffff;
  }
  * { margin: 0; padding: 0; box-sizing: border-box; }
  html, body {
    width: 1200px;
    height: 960px;
    overflow: hidden;
    background: var(--backdrop);
  }
  .book-cover {
    position: absolute;
    left: 320px;
    top: 70px;
    width: 560px;
    height: 820px;
    background: var(--paper);
    overflow: hidden;
    box-shadow: 0 10px 30px rgba(0,0,0,0.18);
  }
  .cover-art {
    position: absolute;
    inset: 0;
    width: 100%;
    height: 100%;
  }
  .author-block {
    position: absolute;
    left: 22px;
    top: 46px;
  }
  .author-intro {
    font-family: "Roboto Condensed", sans-serif;
    font-style: italic;
    font-weight: 300;
    font-size: 27px;
    color: var(--accent-orange);
    line-height: 1.1;
  }
  .author-name {
    margin-top: 6px;
    padding-left: 12px;
    border-left: 4px solid var(--accent-red);
    font-family: "Roboto Condensed", sans-serif;
    font-weight: 700;
    font-size: 27px;
    color: var(--text-light);
    line-height: 1.15;
  }
  .book-title {
    position: absolute;
    left: 28px;
    top: 282px;
    font-family: "Oswald", sans-serif;
    font-weight: 600;
    font-size: 64px;
    line-height: 72px;
    text-transform: uppercase;
  }
  .book-title span { display: block; }
  .title-red { color: var(--accent-red); }
  .title-yellow { color: var(--accent-yellow); }
  .title-white { color: var(--text-light); }
  .publisher {
    position: absolute;
    left: 232px;
    bottom: 30px;
    font-family: "Roboto Condensed", sans-serif;
    font-weight: 400;
    font-size: 20px;
    color: var(--ink);
  }
</style>
</head>
<body>
  <main class="book-cover">
    <svg class="cover-art" viewBox="0 0 560 820" preserveAspectRatio="none" role="img" aria-label="Dark silhouette area with red and yellow offset outlines">
      <polygon fill="var(--accent-yellow)" points="0,0 342,0 528,380 528,470 178,820 0,820"/>
      <polygon fill="var(--accent-red)" points="0,0 328,0 514,380 514,470 164,820 0,820"/>
      <polygon fill="var(--ink)" points="0,0 314,0 500,380 500,470 150,820 0,820"/>
    </svg>

    <header class="author-block">
      <p class="author-intro">The gentle phrases of</p>
      <p class="author-name">Honoré Vasseline</p>
    </header>

    <h1 class="book-title">
      <span class="title-red">Jeux pleins</span>
      <span class="title-yellow">de sens,</span>
      <span class="title-white">sens des</span>
      <span class="title-white">jeux</span>
    </h1>

    <p class="publisher">Editions Plumeau</p>
  </main>
</body>
</html>
```